Plumbing Products Website

This project is to create a web page for Mr. Clear Brook and Mr. Hot Kettle's product offerings. There are 14 unique products. The main page will showcase all 14 products arranged in a clean, concise format that flows nicely and is easy to read.
Furthermore, I need a unique page for each of the 14 products that the main page can link the products to so visitors can click each of them to "Learn More".
For reference, our websites are MrBrookly.example and TopBoilerHub.example; so keep the branding, color-scheme, header, footer, etc. consistent with MrBrookly.example and TopBoilerHub.example.
For reference, here is the catalog. Feel free to copy as much of the content as necessary to build the pages:
https://catalogs.pagefolio.example/MrHotKettle/qvtx/
For clarification, the products are:
1. Whole House Water Purification System
2. Whole House Water Ionization System
3. Whole House Water Softener System
4. Water Heater Sediment Pre-Filter
5. Whole-House UV Water Sterilization System
6. The ULTIMATE Whole House Water Treatment System
7. Under-Sink Reverse Osmosis System with UV Sterilizer
8. Smart Water Heater Regulator with Automated Stand-By for Power Savings
9. Whole House Water Pressure Booster
10. Hot Water Heater Tank Volume Booster
11. Leak Detector with Automatic Water Shutoff
12. Whole House UV Air Purification System
13. Leak Detector Alarm with Mobile App
14. Multi-Gas Detector for Carbon Monoxide, Natural Gas, Propane, Methane, Explosive Gasses, Smoke & Fire
Unfortunately, all the content was created by AI, so I don't have any "original" images or other media. I have attached the logos for your reference though. Also, each individual catalog page is attached.
Once the winning design is chosen, I will need the pages coded and hosted on a staging server for me to view in a live environment before I move them to my server.
Let me know if you have any questions.

```html
<!DOCTYPE html>
<html lang="en">
<head>
<meta charset="utf-8">
<title>Mr. Clear Brook – Products</title>
<link href="https://fonts.googleapis.com/css2?family=Inter:wght@400;500;600;700;800&display=swap" rel="stylesheet">
<style>
:root{
  --navy:#1b3b8c;
  --navy-deep:#0d2a78;
  --teal:#1aa1b4;
  --price:#17a2a8;
  --orange:#ff8a00;
  --orange-2:#ffa51f;
  --text:#2a2f3a;
  --muted:#8a8f99;
  --white:#ffffff;
}
*{box-sizing:border-box;margin:0;padding:0}
html,body{width:1200px;height:4223px;overflow:hidden}
body{font-family:"Inter",sans-serif;color:var(--text);background:var(--white);position:relative}
a{color:inherit;text-decoration:none}

.topbar{position:absolute;left:0;top:0;width:1200px;height:44px;
  background:linear-gradient(90deg,#1d64b8,#1b8fc8 55%,#1fb3bc);
  display:flex;justify-content:flex-end;align-items:center;gap:30px;padding-right:85px;color:#fff;font-size:14px;font-weight:500}
.topbar span{display:flex;align-items:center;gap:10px}
.topbar .ico{width:28px;height:28px;border-radius:50%;background:#fff;display:flex;align-items:center;justify-content:center}

.header{position:absolute;left:0;top:44px;width:1200px;height:94px;background:#fff}
.brand{position:absolute;left:85px;top:26px;display:flex;align-items:center;gap:10px;font-weight:800;font-size:22px;color:var(--navy)}
.brand .dot{width:42px;height:42px;border-radius:50%;background:var(--navy)}
.nav{position:absolute;left:492px;top:38px;display:flex;gap:28px;font-size:15px;font-weight:700;color:#1d2340}
.nav .has-sub{display:flex;align-items:center;gap:6px}
.btn{display:inline-flex;align-items:center;justify-content:space-between;border-radius:24px;font-weight:700;font-size:15px;color:#fff;padding:0 6px 0 26px}
.btn .arrow{width:32px;height:32px;border-radius:50%;background:#fff;display:flex;align-items:center;justify-content:center}
.btn-orange{background:linear-gradient(90deg,var(--orange-2),var(--orange))}
.btn-navy{background:var(--navy-deep)}
.header .btn{position:absolute;left:939px;top:26px;width:174px;height:42px}

.hero{position:absolute;left:0;top:138px;width:1200px;height:673px;
  background:linear-gradient(180deg,#eef7fc 0%,#d8edf9 55%,#9fd0ef 100%)}
.hero-visual{position:absolute;left:640px;top:90px;width:560px;height:583px;
  background:radial-gradient(ellipse at 55% 45%,#2f55c4 0%,#2747a8 45%,#8fc7ee 80%,transparent 100%)}
.hero h1{position:absolute;left:85px;top:162px;font-size:48px;line-height:54px;font-weight:400;color:var(--navy);white-space:nowrap}
.hero h1 strong{display:block;font-weight:800;color:var(--teal)}
.hero .lead{position:absolute;left:85px;top:282px;font-size:19px;line-height:28px;color:#1a1f2b}
.hero .actions{position:absolute;left:85px;top:365px;display:flex;gap:10px}
.hero .actions .btn{height:46px}
.hero .actions .btn-orange{width:177px}
.hero .actions .btn-navy{width:187px}
.badge{position:absolute;left:865px;top:105px;width:142px;height:142px;border-radius:50%;
  background:var(--navy-deep);border:4px solid #fff;box-shadow:0 0 0 3px var(--navy-deep);
  color:#fff;text-align:center;display:flex;flex-direction:column;justify-content:center;font-weight:700}
.badge .small{font-size:12px;line-height:14px}
.badge .big{font-size:38px;line-height:42px;color:#ffc21a;font-weight:800}
.features{position:absolute;left:85px;top:578px;display:flex}
.feature{display:flex;align-items:center;gap:14px;font-size:15px;line-height:18px;font-weight:700;color:var(--navy)}
.feature:nth-child(1){width:238px}
.feature:nth-child(2){width:164px}

.section-head{position:absolute;left:0;top:906px;width:1200px;text-align:center}
.section-head h2{font-size:43px;font-weight:800;color:var(--navy);letter-spacing:.5px}
.section-head h2 span{color:var(--teal)}
.divider{display:block;margin:10px auto 0;width:300px;height:36px}
.section-head p{margin-top:8px;font-size:15px;color:#2a2f3a}

.grid{position:absolute;left:85px;top:1082px;display:grid;grid-template-columns:repeat(3,325px);column-gap:26px;row-gap:25px}
.card{position:relative;height:516px;background:#fff;border-radius:14px;overflow:hidden;box-shadow:0 4px 22px rgba(30,60,120,.10)}
.card .photo{position:absolute;left:40px;right:40px;top:22px;height:210px;border-radius:8px;
  background:radial-gradient(ellipse at center,#c9d3e0 0%,#e8edf3 60%,#fff 100%)}
.card h3{position:absolute;left:25px;right:25px;top:251px;font-size:17.5px;line-height:21px;font-weight:700;color:#1a1f2b}
.card .desc{position:absolute;left:25px;right:40px;top:310px;font-size:15px;line-height:25px;color:#3a3f4a}
.card .price{position:absolute;left:25px;top:370px;font-size:16.5px;font-weight:700;color:var(--price)}
.card .regular{position:absolute;left:25px;top:393px;font-size:13.5px;color:var(--muted)}
.card.tall .desc{top:329px}
.card.tall .price{top:372px}
.card.tall .regular{top:395px}
.card .water{position:absolute;left:0;right:0;bottom:0;height:74px;
  background:linear-gradient(180deg,#bfe2f4 0%,#d9eef9 30%,#b7ddf3 100%)}
.card .more{position:absolute;left:25px;bottom:20px;display:flex;align-items:center;gap:10px;font-size:15px;font-weight:700;color:var(--orange)}
.card.wide{grid-column:1/4;height:339px}
.card.wide .photo{left:800px;right:20px;top:30px;height:200px}
.card.wide h3{top:56px;right:300px}
.card.wide .desc{top:106px}
.card.wide .price{top:150px}
.card.wide .regular{top:174px}
.card.wide .water{height:104px}

.footer{position:absolute;left:0;top:3712px;width:1200px;height:511px;color:#fff}
.footer .wave{position:absolute;left:0;top:0;width:1200px;height:511px}
.f-brand{position:absolute;left:85px;top:150px;width:160px;font-size:20px;font-weight:800;line-height:24px;text-align:center}
.f-brand .dot{display:block;margin:0 auto 10px;width:80px;height:80px;border-radius:50%;background:#2d5bd0}
.socials{position:absolute;left:103px;top:302px;display:flex;gap:10px}
.socials span{width:34px;height:34px;border-radius:50%;background:#fff}
.f-col{position:absolute;top:140px}
.f-col h4{font-size:18px;font-weight:700;margin-bottom:20px}
.f-col li{list-style:none;font-size:15.5px;line-height:34px}
.f-col.company{left:315px}
.f-col.legal{left:477px}
.f-col.contact{left:656px}
.contact li{display:flex;align-items:flex-start;gap:14px;line-height:22px;margin-bottom:20px}
.contact .ico{flex:none;width:34px;height:34px;border-radius:50%;background:#1aa0d8;display:flex;align-items:center;justify-content:center}
.contact li span{padding-top:6px}
.f-brand2{position:absolute;left:950px;top:165px;width:170px;text-align:center;font-size:20px;font-weight:800;line-height:24px}
.f-brand2 .dot{display:block;margin:0 auto 10px;width:80px;height:80px;border-radius:50%;background:#2d5bd0}
.f-rule{position:absolute;left:85px;top:446px;width:1028px;height:1px;background:rgba(255,255,255,.25)}
.copyright{position:absolute;left:0;top:466px;width:1200px;text-align:center;font-size:15px}
</style>
</head>
<body>

<div class="topbar">
  <span><i class="ico"><svg width="14" height="14" viewBox="0 0 24 24"><path fill="#1d64b8" d="M6.6 10.8a15 15 0 006.6 6.6l2.2-2.2a1 1 0 011-.25 11.4 11.4 0 003.6.6 1 1 0 011 1V20a1 1 0 01-1 1A17 17 0 013 4a1 1 0 011-1h3.5a1 1 0 011 1 11.4 11.4 0 00.6 3.6 1 1 0 01-.25 1z"/></svg></i>Phone: 555-300-0175</span>
  <span><i class="ico"><svg width="14" height="14" viewBox="0 0 24 24"><path fill="#1d64b8" d="M3 5h18v14H3z"/><path d="M3 6l9 7 9-7" stroke="#fff" stroke-width="2" fill="none"/></svg></i>info@topboilerhub.example</span>
</div>

<header class="header">
  <a class="brand" href="#"><span class="dot"></span>Mr. Clear Brook</a>
  <nav class="nav">
    <a href="#">HOME</a>
    <a href="#" class="has-sub">PRODUCTS <svg width="10" height="8" viewBox="0 0 10 8"><path d="M1 2l4 4 4-4" stroke="#1d2340" stroke-width="1.6" fill="none"/></svg></a>
    <a href="#">ABOUT</a>
    <a href="#">CONTACT</a>
  </nav>
  <a class="btn btn-orange" href="#">GET QUOTE <span class="arrow"><svg width="14" height="14" viewBox="0 0 14 14"><path d="M2 7h10M8 3l4 4-4 4" stroke="#ff8a00" stroke-width="2" fill="none"/></svg></span></a>
</header>

<section class="hero" role="img" aria-label="Blue water splash background">
  <div class="hero-visual" role="img" aria-label="Plumber in blue uniform holding a whole house water filter"></div>
  <h1>WHOLE HOUSE WATER<strong>PURIFICATION SYSTEM</strong></h1>
  <p class="lead">Cleaner water for drinking,Bathing, and every appliance<br>In your home,</p>
  <div class="actions">
    <a class="btn btn-orange" href="#">GET QUOTE <span class="arrow"><svg width="14" height="14" viewBox="0 0 14 14"><path d="M2 7h10M8 3l4 4-4 4" stroke="#ff8a00" stroke-width="2" fill="none"/></svg></span></a>
    <a class="btn btn-navy" href="#">LEARN MORE <span class="arrow"><svg width="14" height="14" viewBox="0 0 14 14"><path d="M2 7h10M8 3l4 4-4 4" stroke="#0d2a78" stroke-width="2" fill="none"/></svg></span></a>
  </div>
  <div class="badge">
    <span class="small">REMOVES<br>UP TO</span>
    <span class="big">99.9%</span>
    <span class="small">OF IMPURITIES!</span>
  </div>
  <div class="features">
    <div class="feature"><svg width="52" height="52" viewBox="0 0 52 52"><circle cx="26" cy="26" r="23" stroke="#1b3b8c" stroke-width="2" fill="none"/><path d="M26 13c5 7 8 11 8 15a8 8 0 01-16 0c0-4 3-8 8-15z" stroke="#1b3b8c" stroke-width="2" fill="none"/></svg>CLEANER<br>DRINKING WATER</div>
    <div class="feature"><svg width="40" height="52" viewBox="0 0 40 52"><path d="M8 50V10a6 6 0 016-6h6a6 6 0 016 6v4" stroke="#1b3b8c" stroke-width="2.4" fill="none"/><path d="M18 16h16" stroke="#1b3b8c" stroke-width="2.4"/><path d="M22 24v4M28 24v4M34 24v4" stroke="#1b3b8c" stroke-width="2.4"/></svg>BETTER<br>SHOWERS</div>
    <div class="feature"><svg width="44" height="52" viewBox="0 0 44 52"><path d="M22 4l18 6v14c0 12-8 20-18 24C12 44 4 36 4 24V10z" stroke="#1b3b8c" stroke-width="2.4" fill="none"/><path d="M14 26l6 6 10-12" stroke="#1b3b8c" stroke-width="2.4" fill="none"/></svg>PROTECTS<br>APPLIANCES</div>
  </div>
</section>

<div class="section-head">
  <h2>OUR <span>PRODUCT</span></h2>
  <svg class="divider" viewBox="0 0 300 36"><path d="M0 18h130M170 18h130" stroke="#1aa1b4" stroke-width="2"/><circle cx="150" cy="18" r="15" stroke="#1b3b8c" stroke-width="2" fill="#fff"/><path d="M150 9c4 6 6 9 6 12a6 6 0 01-12 0c0-3 2-6 6-12z" fill="#1b3b8c"/></svg>
  <p>Softer water. Better life. Protection that lasts.</p>
</div>

<main class="grid">
  <article class="card"><div class="photo" role="img" aria-label="Inline ionization cartridge with copper fittings"></div>
    <h3>Whole House Water<br>Ionization System</h3><p class="desc">Softer water. Better life. Protection that lasts.</p>
    <p class="price">$795 Installed</p><p class="regular">Regular <s>$1200</s></p>
    <div class="water" role="img" aria-label="Water surface"></div><a class="more" href="#">LEARN MORE <svg width="14" height="10" viewBox="0 0 14 10"><path d="M1 5h11M8 1l4 4-4 4" stroke="#ff8a00" stroke-width="1.8" fill="none"/></svg></a></article>

  <article class="card"><div class="photo" role="img" aria-label="Water softener tank with resin cutaway"></div>
    <h3>Whole House Water<br>Softener System</h3><p class="desc">Softer water. Better life. Protection that lasts.</p>
    <p class="price">$1995 Installed</p><p class="regular">Regular <s>$3000</s></p>
    <div class="water" role="img" aria-label="Water surface"></div><a class="more" href="#">LEARN MORE <svg width="14" height="10" viewBox="0 0 14 10"><path d="M1 5h11M8 1l4 4-4 4" stroke="#ff8a00" stroke-width="1.8" fill="none"/></svg></a></article>

  <article class="card"><div class="photo" role="img" aria-label="Blue sediment pre-filter housing"></div>
    <h3>Water Heater Sediment<br>Pre-Filter</h3><p class="desc">Stops Large Particles Before They Enter Your Tank</p>
    <p class="price">$495 Installed</p><p class="regular">Regular <s>$850</s></p>
    <div class="water" role="img" aria-label="Water surface"></div><a class="more" href="#">LEARN MORE <svg width="14" height="10" viewBox="0 0 14 10"><path d="M1 5h11M8 1l4 4-4 4" stroke="#ff8a00" stroke-width="1.8" fill="none"/></svg></a></article>

  <article class="card"><div class="photo" role="img" aria-label="Stainless UV sterilizer tube with copper fittings"></div>
    <h3>Whole-House UV Water<br>Sterilization System</h3><p class="desc">Kills viruses, germs, bacteria &amp; organisms</p>
    <p class="price">$1495 Installed</p><p class="regular">Regular <s>$2000</s></p>
    <div class="water" role="img" aria-label="Water surface"></div><a class="more" href="#">LEARN MORE <svg width="14" height="10" viewBox="0 0 14 10"><path d="M1 5h11M8 1l4 4-4 4" stroke="#ff8a00" stroke-width="1.8" fill="none"/></svg></a></article>

  <article class="card"><div class="photo" role="img" aria-label="Vertical whole house treatment unit"></div>
    <h3>The ULTIMATE Whole House<br>Water Treatment System</h3><p class="desc">Three powerful systems. One complete solution.</p>
    <p class="price">$2995 Installed</p><p class="regular">Regular <s>$4000</s></p>
    <div class="water" role="img" aria-label="Water surface"></div><a class="more" href="#">LEARN MORE <svg width="14" height="10" viewBox="0 0 14 10"><path d="M1 5h11M8 1l4 4-4 4" stroke="#ff8a00" stroke-width="1.8" fill="none"/></svg></a></article>

  <article class="card"><div class="photo" role="img" aria-label="Stacked reverse osmosis filter stages with splash"></div>
    <h3>Under-Sink Reverse Osmosis<br>System with UV Sterilizer</h3><p class="desc">Pure. Healthy. Great-tasting water - Right from your tap.</p>
    <p class="price">$1495 Installed</p><p class="regular">Regular <s>$2000</s></p>
    <div class="water" role="img" aria-label="Water surface"></div><a class="more" href="#">LEARN MORE <svg width="14" height="10" viewBox="0 0 14 10"><path d="M1 5h11M8 1l4 4-4 4" stroke="#ff8a00" stroke-width="1.8" fill="none"/></svg></a></article>

  <article class="card tall"><div class="photo" role="img" aria-label="Water heater timer unit and phone app"></div>
    <h3>Smart Water Heater Regulator<br>with Automated Stand-By<br>for Power Savings</h3><p class="desc">To save energy by upto 50%</p>
    <p class="price">$395 Installed</p><p class="regular">Regular <s>$650</s></p>
    <div class="water" role="img" aria-label="Water surface"></div><a class="more" href="#">LEARN MORE <svg width="14" height="10" viewBox="0 0 14 10"><path d="M1 5h11M8 1l4 4-4 4" stroke="#ff8a00" stroke-width="1.8" fill="none"/></svg></a></article>

  <article class="card"><div class="photo" role="img" aria-label="Compact black and white pressure booster pump"></div>
    <h3>Whole House Water<br>Pressure Booster</h3><p class="desc">Strong steady pressure from every fixture</p>
    <p class="price">$1495 Installed</p><p class="regular">Regular <s>$2000</s></p>
    <div class="water" role="img" aria-label="Water surface"></div><a class="more" href="#">LEARN MORE <svg width="14" height="10" viewBox="0 0 14 10"><path d="M1 5h11M8 1l4 4-4 4" stroke="#ff8a00" stroke-width="1.8" fill="none"/></svg></a></article>

  <article class="card"><div class="photo" role="img" aria-label="Brass mixing valve with gauge"></div>
    <h3>Hot Water Heater Tank<br>Volume Booster</h3><p class="desc">Get up to 50% more hot water Without a larger tank!</p>
    <p class="price">$449 Installed</p><p class="regular">Regular <s>$600</s></p>
    <div class="water" role="img" aria-label="Water surface"></div><a class="more" href="#">LEARN MORE <svg width="14" height="10" viewBox="0 0 14 10"><path d="M1 5h11M8 1l4 4-4 4" stroke="#ff8a00" stroke-width="1.8" fill="none"/></svg></a></article>

  <article class="card"><div class="photo" role="img" aria-label="Round white leak sensor with probe cable"></div>
    <h3>Leak Detector with Automatic<br>Water Shutoff</h3><p class="desc">Detects Leaks. Stops Damage. Shuts Off Water. Automatically.</p>
    <p class="price">$995 Installed</p><p class="regular">Regular <s>$1500</s></p>
    <div class="water" role="img" aria-label="Water surface"></div><a class="more" href="#">LEARN MORE <svg width="14" height="10" viewBox="0 0 14 10"><path d="M1 5h11M8 1l4 4-4 4" stroke="#ff8a00" stroke-width="1.8" fill="none"/></svg></a></article>

  <article class="card"><div class="photo" role="img" aria-label="UV-C lamp unit inside an HVAC duct"></div>
    <h3>Whole House UV Air<br>Purification System</h3><p class="desc">Dual UV-C lights continuously sanitize air inside your HVAC</p>
    <p class="price">$395 Installed</p><p class="regular">Regular <s>$800</s></p>
    <div class="water" role="img" aria-label="Water surface"></div><a class="more" href="#">LEARN MORE <svg width="14" height="10" viewBox="0 0 14 10"><path d="M1 5h11M8 1l4 4-4 4" stroke="#ff8a00" stroke-width="1.8" fill="none"/></svg></a></article>

  <article class="card"><div class="photo" role="img" aria-label="Small white leak alarm sensor"></div>
    <h3>Leak Detector Alarm with<br>Mobile App</h3><p class="desc">Get up to 50% more hot water Without a larger tank!</p>
    <p class="price">$195 Installed</p><p class="regular">Regular <s>$350</s></p>
    <div class="water" role="img" aria-label="Water surface"></div><a class="more" href="#">LEARN MORE <svg width="14" height="10" viewBox="0 0 14 10"><path d="M1 5h11M8 1l4 4-4 4" stroke="#ff8a00" stroke-width="1.8" fill="none"/></svg></a></article>

  <article class="card wide"><div class="photo" role="img" aria-label="Black multi-gas detector with digital display"></div>
    <h3>Multi-Gas Detector for Carbon Monoxide, Natural Gas, Propane, Methane, Explosive Gasses, Smoke &amp; Fire</h3><p class="desc">One Smart Alarm For Gas, Carbon Monoxide, Smoke &amp; Fire Safety</p>
    <p class="price">$195 Installed</p><p class="regular">Regular <s>$300</s></p>
    <div class="water" role="img" aria-label="Water surface"></div><a class="more" href="#">LEARN MORE <svg width="14" height="10" viewBox="0 0 14 10"><path d="M1 5h11M8 1l4 4-4 4" stroke="#ff8a00" stroke-width="1.8" fill="none"/></svg></a></article>
</main>

<footer class="footer">
  <svg class="wave" viewBox="0 0 1200 511" preserveAspectRatio="none"><defs><linearGradient id="fg" x1="0" y1="0" x2="0" y2="1"><stop offset="0" stop-color="#123a9a"/><stop offset="1" stop-color="#0b2470"/></linearGradient></defs><path d="M0 60C200 100 420 20 640 30C860 40 1000 -10 1200 20V511H0z" fill="url(#fg)"/></svg>
  <div class="f-brand"><span class="dot"></span>Mr. Clear Brook</div>
  <div class="socials"><span aria-label="Social profile"></span><span aria-label="Social profile"></span><span aria-label="Social profile"></span></div>
  <div class="f-col company"><h4>Company</h4><ul><li>Home</li><li>Products</li><li>About</li><li>Contact</li></ul></div>
  <div class="f-col legal"><h4>Legal Links</h4><ul><li>Sitemap</li><li>Privacy Policy</li><li>Terms of Use</li></ul></div>
  <div class="f-col contact"><h4>Contact Us</h4><ul>
    <li><i class="ico"><svg width="14" height="14" viewBox="0 0 24 24"><path fill="#fff" d="M6.6 10.8a15 15 0 006.6 6.6l2.2-2.2a1 1 0 011-.25 11.4 11.4 0 003.6.6 1 1 0 011 1V20a1 1 0 01-1 1A17 17 0 013 4a1 1 0 011-1h3.5a1 1 0 011 1 11.4 11.4 0 00.6 3.6 1 1 0 01-.25 1z"/></svg></i><span>555-300-0175</span></li>
    <li><i class="ico"><svg width="14" height="14" viewBox="0 0 24 24"><path fill="#fff" d="M3 5h18v14H3z"/><path d="M3 6l9 7 9-7" stroke="#1aa0d8" stroke-width="2" fill="none"/></svg></i><span>info@topboilerhub.example</span></li>
    <li><i class="ico"><svg width="14" height="16" viewBox="0 0 24 28"><path fill="#fff" d="M12 1a9 9 0 019 9c0 7-9 17-9 17S3 17 3 10a9 9 0 019-9z"/><circle cx="12" cy="10" r="3.5" fill="#1aa0d8"/></svg></i><span>742 Marlow Ave., Suite 8<br>Seabright, FL, 33400</span></li>
  </ul></div>
  <div class="f-brand2"><span class="dot"></span>Mr. Hot Kettle</div>
  <div class="f-rule"></div>
  <p class="copyright">Copyright © 2026 Mr. Clear Brook. All Rights Reserved</p>
</footer>

</body>
</html>
```